Brass Kite Gig - 20 Years of Funk

I'm with a funk band called Brass Kite. We are celebrating our 20 year anniversary with a show on August 3, 2024. We would like some banners made for social media to help promote the gig. I'm attaching some examples of our 10 year anniversary gig so you can at least get an idea of what we are looking for.

Here's the text for the banners:
BRASS KITE Anniversary Gig - 20 Years of Funk!
Saturday, August 10, 2024
with special guest: Marco Delvin
Doors at 7pm, Show at 8pm

We would like three sizes:
1920 x 1005 pixels
1080 x 1080 pixels
1080 x 1920 pixels

You can check out our website for more ideas of our graphic style, etc.. www.brasskiteband.example

```html
<!DOCTYPE html>
<html lang="en">
<head>
<meta charset="utf-8">
<title>Brass Kite – 20 Years of Funk banners</title>
<link rel="stylesheet" href="https://fonts.googleapis.com/css2?family=Bebas+Neue&family=Mr+Dafoe&display=swap">
<style>
:root{
  --lime:#c6dc2c;
  --ink:#07060c;
  --night:#0d0a1e;
  --violet:#5b2a9c;
  --paper:#ffffff;
  --stage:#959595;
}
*{box-sizing:border-box;margin:0;padding:0}
html,body{width:1200px;height:1117px;overflow:hidden;background:var(--stage)}
body{position:relative;font-family:"Bebas Neue",sans-serif;color:var(--paper)}
.banner{position:absolute;overflow:hidden;background:var(--ink);box-shadow:6px 8px 14px rgba(0,0,0,.35)}
.banner > *{position:absolute}
.stage-photo{inset:0;background:
  radial-gradient(ellipse at 55% 10%,rgba(140,70,220,.65),transparent 55%),
  radial-gradient(ellipse at 80% 60%,rgba(110,50,180,.5),transparent 50%),
  radial-gradient(ellipse at 20% 75%,rgba(80,40,140,.45),transparent 50%),
  linear-gradient(180deg,var(--night),#1a0f35 60%,var(--ink))}
.band-name{color:var(--lime);line-height:1;white-space:nowrap;letter-spacing:.02em}
.gig-frame{
  border:2px solid var(--paper);border-radius:28px;
  -webkit-mask-image:linear-gradient(to right,#000 16%,transparent 16%,transparent 84%,#000 84%),linear-gradient(#000,#000);
  -webkit-mask-size:100% 6px,100% calc(100% - 6px);
  -webkit-mask-position:top,bottom;
  -webkit-mask-repeat:no-repeat;
  mask-image:linear-gradient(to right,#000 16%,transparent 16%,transparent 84%,#000 84%),linear-gradient(#000,#000);
  mask-size:100% 6px,100% calc(100% - 6px);
  mask-position:top,bottom;
  mask-repeat:no-repeat;
}
.gig-title{text-align:center;line-height:.95;white-space:nowrap;font-weight:400}
.gig-title .kicker{display:block}
.gig-title .years{display:block;color:var(--lime)}
.gig-title .funk{display:block}
.event-date{display:flex;align-items:flex-end;gap:.15em;line-height:.88;white-space:nowrap}
.event-date .year{color:var(--lime);line-height:.8}
.guest-tag{background:var(--lime);color:var(--ink);line-height:1;padding:2px 4px;white-space:nowrap}
.guest-name{font-family:"Mr Dafoe",cursive;line-height:1;white-space:nowrap}
.times{border:2px solid var(--lime);background:var(--ink);display:flex;align-items:center;justify-content:center;gap:.6em;white-space:nowrap}
.times::after{content:"";position:absolute;left:6px;top:6px;right:-6px;bottom:-6px;border-right:2px solid var(--paper);border-bottom:2px solid var(--paper);pointer-events:none}
.paper-strip{left:0;right:0;bottom:0;background:var(--paper)}
.badge{border-radius:50%;background:var(--ink);border:6px solid var(--lime)}
.site-url{color:var(--ink);white-space:nowrap;line-height:1}
</style>
</head>
<body>

<!-- Landscape 1920 x 1005 -->
<section class="banner banner--landscape" style="left:205px;top:48px;width:596px;height:312px">
  <div class="stage-photo" role="img" aria-label="Band performing on a purple-lit stage"></div>
  <div class="band-name" style="left:33px;top:31px;font-size:56px">Brass Kite</div>
  <div class="gig-frame" style="left:30px;top:114px;width:264px;height:124px"></div>
  <h1 class="gig-title" style="left:30px;top:104px;width:264px;font-size:22px">
    <span class="kicker">Anniversary Gig -</span>
    <span class="years" style="font-size:60px">20 Years</span>
    <span class="funk" style="font-size:32px">of Funk!</span>
  </h1>
  <div class="event-date" style="left:328px;top:28px;font-size:29px">
    <span>Saturday,<br>August 10,</span><span class="year" style="font-size:68px">2024</span>
  </div>
  <div class="guest-tag" style="left:406px;top:94px;font-size:9px">With special guest:</div>
  <div class="guest-name" style="left:316px;top:96px;font-size:52px">Marco Delvin</div>
  <div class="times" style="left:343px;top:156px;width:209px;height:30px;font-size:19px"><span>Doors at 7pm</span><span>|</span><span>Show at 8p</span></div>
  <div class="paper-strip" style="height:58px"></div>
  <div class="badge" style="left:29px;top:211px;width:92px;height:92px"></div>
  <div class="site-url" style="left:367px;top:278px;font-size:20px">www.brasskiteband.example</div>
</section>

<!-- Portrait 1080 x 1920 -->
<section class="banner banner--portrait" style="left:205px;top:375px;width:391px;height:694px">
  <div class="stage-photo" role="img" aria-label="Band performing on a purple-lit stage"></div>
  <div class="band-name" style="left:0;width:391px;text-align:center;top:20px;font-size:82px">Brass Kite</div>
  <div class="gig-frame" style="left:33px;top:123px;width:323px;height:152px"></div>
  <h1 class="gig-title" style="left:33px;top:110px;width:323px;font-size:28px">
    <span class="kicker">Anniversary Gig -</span>
    <span class="years" style="font-size:76px">20 Years</span>
    <span class="funk" style="font-size:42px">of Funk!</span>
  </h1>
  <div class="event-date" style="left:60px;top:406px;font-size:34px">
    <span>Saturday,<br>August 10,</span><span class="year" style="font-size:80px">2024</span>
  </div>
  <div class="guest-tag" style="left:151px;top:485px;font-size:10px">With special guest:</div>
  <div class="guest-name" style="left:40px;top:486px;font-size:60px">Marco Delvin</div>
  <div class="times" style="left:78px;top:556px;width:244px;height:36px;font-size:22px"><span>Doors at 7pm</span><span>|</span><span>Show at 8p</span></div>
  <div class="paper-strip" style="height:74px"></div>
  <div class="badge" style="left:12px;top:596px;width:88px;height:88px"></div>
  <div class="site-url" style="left:116px;top:654px;font-size:22px">www.brasskiteband.example</div>
</section>

<!-- Square 1080 x 1080 -->
<section class="banner banner--square" style="left:615px;top:375px;width:388px;height:388px">
  <div class="stage-photo" role="img" aria-label="Band performing on a purple-lit stage"></div>
  <div class="band-name" style="left:34px;top:24px;font-size:54px">Brass Kite</div>
  <div class="gig-frame" style="left:31px;top:107px;width:205px;height:96px;border-radius:22px"></div>
  <h1 class="gig-title" style="left:31px;top:98px;width:205px;font-size:18px">
    <span class="kicker">Anniversary Gig -</span>
    <span class="years" style="font-size:49px">20 Years</span>
    <span class="funk" style="font-size:27px">of Funk!</span>
  </h1>
  <div class="event-date" style="left:249px;top:107px;font-size:28px;flex-direction:column;align-items:flex-start;gap:2px">
    <span>Saturday,<br>August 10,</span><span class="year" style="font-size:56px;margin-left:5px">2024</span>
  </div>
  <div class="guest-tag" style="left:148px;top:220px;font-size:9px">With special guest:</div>
  <div class="guest-name" style="left:32px;top:222px;font-size:56px">Marco Delvin</div>
  <div class="paper-strip" style="height:40px"></div>
  <div class="times" style="left:166px;top:288px;width:187px;height:26px;font-size:16px"><span>Doors at 7pm</span><span>|</span><span>Show at 8p</span></div>
  <div class="badge" style="left:71px;top:274px;width:97px;height:97px"></div>
  <div class="site-url" style="left:224px;top:361px;font-size:16px">www.brasskiteband.example</div>
</section>

</body>
</html>
```